Brightmoor Pathways

We need a website designed for a life coaching company who specialises in one on one coaching, workshops and seminars where they teach participants in goal setting and how to achieve them for a better life.

Objectives

·         Easy to use

·         Clear & concise

·         Quality but not too flashy

·         Shows clearly what you do and how you interact with clients

·         No fuss, straight up

·         Gives those who hear your name or business name a place to go to obtain further information on what I am doing, why & how they can use my services.

·         A way for clients to contact you

·         Seminar & workshop bookings (not mandatory)

·         Most of the website to be static.

Number of Pages Required

1 page

Requirements
Must have
• Sitemap

• Home
• About Us
• One on One Coaching
• Workshops/Seminars
• How we Work?
• Pricing
• Testimonials
• Contact Us

• Design/Content Brief

• ü  The following elements are included in the design/content brief which this proposal is based on:

• o    Flash banner with some images rotating that reflect your business.

• o    Logo and phone number 0438 760 214 will be prominently displayed.

• o    Horizontal Navigation

• o    Contact Us icon on homepage

• o    Sign up for our newsletter on homepage

• o    Privacy Policy/Sitemap/Terms & Conditions in footer

• o    - larger rounded buttons

• o    - good size font

• o    - not having to scroll too far

• o    - soft feel, but not fluffy (images will enhance this)

• ü  Colours that could be used with logo

• o   What about this?  RGB 128,128,128

• o   What about this?  RGB 54, 95, 145

• o   What about this?  RGB 51, 204, 51

• o   Red – R255

• ü   http://www.plumvexlo.com/

• o    I like this website and its rounded buttons, large easy to see and use.

• o    Soft colours

• o    Changing pictures at the top of screen

• Files

```html
<!DOCTYPE html>
<html lang="en">
<head>
<meta charset="utf-8">
<title>Brightmoor Pathways – Life Coaching</title>
<link href="https://fonts.googleapis.com/css2?family=Arimo&family=Marcellus&family=Tinos:wght@400;700&display=swap" rel="stylesheet">
<style>
:root{
  --band:#e4e2d4;
  --band-top:#d5d3c0;
  --red:#e2001a;
  --red-deep:#c40000;
  --red-field:#a80000;
  --ink:#333;
  --grey:#8a8878;
  --nav-top:#7b7a6a;
  --nav-bot:#2c2f27;
  --cream:#efece0;
}
*{box-sizing:border-box;margin:0;padding:0}
html,body{width:1200px;height:852px;overflow:hidden;background:#fff}
body{position:relative;font-family:"Arimo",Arial,sans-serif;color:var(--ink)}
.top-band{position:absolute;left:0;top:0;width:1200px;height:145px;background:var(--band);border-top:9px solid var(--band-top)}
.utility{position:absolute;top:17px;right:150px;display:flex;align-items:center;height:20px;white-space:nowrap}
.utility .brand{font-family:"Tinos",serif;font-weight:700;color:var(--red);font-size:17px;letter-spacing:1px;padding-right:10px}
.utility .phone{font-family:"Tinos",serif;font-weight:700;color:var(--grey);font-size:16px;border-left:1px solid #b7b4a2;border-right:1px solid #b7b4a2;padding:0 8px;margin-right:8px}
.utility .contact{display:flex;align-items:center;gap:7px;font-size:11px;color:var(--grey);text-decoration:none}
.logo{position:absolute;left:150px;top:45px;width:144px;height:122px;border-radius:7px;background:linear-gradient(135deg,#fff,var(--cream));border:1px solid #d2cfbd;display:flex;align-items:center;justify-content:center;text-align:center;font-family:"Tinos",serif;font-size:20px;line-height:1.15;color:var(--red)}
.banner{position:absolute;left:301px;top:45px;width:749px;height:122px;border-radius:7px;background:linear-gradient(#8fa9c8 0%,#dfe5ea 45%,#8fae4c 70%,#5e8a2a 100%)}
.nav{position:absolute;left:150px;top:173px;display:flex;gap:6px;list-style:none}
.nav a{display:flex;align-items:flex-end;justify-content:flex-end;text-align:right;width:145px;height:58px;border-radius:7px;padding:0 11px 7px;background:linear-gradient(var(--nav-top),var(--nav-bot));color:#e8e6dc;font-family:"Marcellus",serif;font-size:17px;line-height:22px;text-decoration:none;white-space:nowrap}
.content{position:absolute;left:150px;top:258px;width:593px}
.content h1{font-family:"Tinos",serif;font-weight:400;font-size:34px;line-height:38px;display:inline-block;border-bottom:4px solid var(--red);padding-bottom:4px;margin-bottom:27px}
.content .photo{float:left;width:298px;height:204px;border-radius:7px;border:1px solid #ccc;background:linear-gradient(#3a6a88 0%,#9bb6c2 40%,#6e8e43 60%,#48652a 100%);margin:2px 10px 4px 0}
.content p{font-size:12.5px;line-height:16.7px;color:#444;margin-bottom:17px}
.signup{position:absolute;left:754px;top:262px;width:296px;height:251px;border-radius:7px;background:linear-gradient(var(--red-deep),#f81800)}
.signup h2{display:flex;align-items:flex-start;white-space:nowrap;font-family:"Marcellus",serif;font-weight:400;color:#f0806a;font-size:42px;line-height:44px;padding:10px 0 0 16px;height:77px;border-bottom:1px solid #b80000}
.signup h2 small{font-size:21px;line-height:19px;color:#4a0800;margin:15px 0 0 6px}
.field{position:absolute;left:12px;display:flex;align-items:center;width:272px}
.field label{width:122px;color:#fff;font-size:13px;line-height:14px}
.field span{width:150px;height:26px;background:var(--red-field);color:#fff;font-size:11px;padding:6px 7px;overflow:hidden;white-space:nowrap}
.signup .rule{position:absolute;left:0;top:199px;width:296px;border-top:1px solid #e21800}
.signup .update{position:absolute;left:12px;top:211px;width:74px;height:26px;background:linear-gradient(#3a3a36,#141412);color:#aaa;font-size:12px;padding:6px 10px;border:none;font-family:inherit;text-align:left}
.join{position:absolute;left:775px;top:529px;width:250px;height:70px;border-radius:6px;background:linear-gradient(#fbfaf4,#d8d5bf);border:1px solid #cbc8b3;font-family:"Marcellus",serif;padding:5px 10px;text-decoration:none;white-space:nowrap;overflow:hidden}
.join .big{color:#c8201c;font-size:29px;line-height:32px}
.join .big em{font-style:normal;color:#555;font-size:22px}
.join .small{color:#999682;font-size:18px;line-height:22px;padding-left:18px}
.footer-band{position:absolute;left:150px;top:701px;width:900px;height:123px;border-radius:7px;background:linear-gradient(#eceae0,#d9d6c6 85%,#bab7a6)}
.footer-band .name{position:absolute;left:15px;top:64px;border-top:4px solid #8c8b82;padding-top:6px;font-family:"Tinos",serif;font-weight:700;font-size:27px;letter-spacing:2.5px;color:#3a3a35;white-space:nowrap}
.legal{position:absolute;right:150px;top:829px;font-size:10px;color:#333;white-space:nowrap}
.legal b{color:var(--red)}
.legal .copy{color:var(--red)}
</style>
</head>
<body>
<div class="top-band"></div>
<div class="utility">
  <span class="brand">Brightmoor Pathways</span>
  <span class="phone">0438 760 214</span>
  <a class="contact" href="#contact">
    <svg width="20" height="13" viewBox="0 0 20 13"><rect x="0.5" y="0.5" width="19" height="12" fill="#fff" stroke="#b7b4a2"/><path d="M0.5 0.5 L10 7 L19.5 0.5" fill="none" stroke="#b7b4a2"/></svg>
    CONTACT US
  </a>
</div>
<div class="logo">Brightmoor<br>Pathways</div>
<div class="banner" role="img" aria-label="Rotating banner photo of a wooden fence across a green meadow under a cloudy sky"></div>
<ul class="nav">
  <li><a href="#">About Us</a></li>
  <li><a href="#">One-On-One<br>Coaching</a></li>
  <li><a href="#">Workshop<br>Seminars</a></li>
  <li><a href="#">How we work?</a></li>
  <li><a href="#">Pricing</a></li>
  <li><a href="#">Testimonials</a></li>
</ul>
<main class="content">
  <h1>Lorem ipsum dolor sit amet</h1>
  <div class="photo" role="img" aria-label="Photo of a coastal path with a wooden rail leading down to the sea"></div>
  <p>Maecenas nisi tellus, imperdiet ut laoreet convallis, ornare quis quam. Quisque purus augue, sagittis id luctus vitae, viverra sed nisl. Phasellus sapien urna, interdum eu fringilla eu, mattis et massa. Donec sem felis, consequat a luctus ac, pharetra vel leo. Duis mollis egestas massa. Suspendisse rhoncus massa a quam pulvinar malesuada. Morbi ac posuere felis. Donec elementum mattis elit nec interdum. Etiam sed mauris eros. Vivamus elem entum blandit nisl, id tempor eros suscipit non. Aliquam dapibus est quis est iaculis a pulvinar est aliquet. Etiam et scelerisque risus. Aenean iaculis velit molestie scelerisque risus. Aenean iaculis velit molestie lorem pharetra gravida.</p>
  <p>Donec ac tortor augue. Vestibulum condimentum tincidunt ligula. Ut consectetur gravida porttitor. Phasellus orci sapien, placerat nec pulvinar ultricies, sodales quis augue. Mauris nisl risus, facilisis quis sagittis vitae, dapibus non mauris. Nullam nec nisl libero. Cum sociis natoque penatibus et magnis dis parturient montes, nascetur ridiculus mus. Vestibulum nec egestas massa. Fusce eges-</p>
</main>
<aside class="signup">
  <h2>Sing up <small>for our<br>newsletter</small></h2>
  <div class="field" style="top:96px"><label>E-MAIL ADDRESS</label><span>hello@brightmoor.com</span></div>
  <div class="field" style="top:133px"><label>CONFIRM E-MAIL ADDRESS</label><span></span></div>
  <div class="field" style="top:169px"><label>PASSWORD</label><span></span></div>
  <div class="rule" style="top:210px"></div>
  <button class="update" style="top:221px">UPDATE</button>
</aside>
<a class="join" href="#">
  <div class="big">Join us <em>this month</em></div>
  <div class="small">workshops &amp; seminars</div>
</a>
<footer>
  <div class="footer-band"><div class="name">Brightmoor Pathways</div></div>
  <div class="legal">Privacy Policy &nbsp;|&nbsp; Terms &amp; Conditions &nbsp;|&nbsp; <span class="copy">Copyrigth <b>Brightmoor Pathways</b> 2009</span></div>
</footer>
</body>
</html>
```